Multifamily Investment Strategies

I need a pamphlet or booklet for multifamily commercial real estate investment.

The specific investment vehicle is affordable multifamily apartments. I have uploaded a 5 page pdf detailing my investment strategy.

The target audience for this pamphlet are investors, commercial brokers, and commercial bankers.

I am looking for modern, clean design that is striking and professional but also eye catching.
Updates

I made a few changes to the brief and also corrected two errors.

Target Market(s)

Commercial Real Estate Investors, Brokers, and Bankers

Industry/Entity Type

Real Estate

Font styles to use
Serif

Colors

Designer to choose colors to be used in the design.

Requirements
Must have
• Graphics of or related to apartment buildings.
• My headshot seen on the last page of the pdf
Nice to have
• Imagery related to investment and profits.
Should not have
• The image of an apartment building on the first page of the pdf is just an example. Please don’t use this image.

```html
<!DOCTYPE html>
<html lang="en">
<head>
<meta charset="utf-8">
<title>Multifamily Cashflow Investment Strategy</title>
<link href="https://fonts.googleapis.com/css2?family=PT+Sans:wght@400;700&family=PT+Sans+Narrow:wght@400;700&family=Saira+Condensed:wght@600&family=Saira+Extra+Condensed:wght@300;400&display=swap" rel="stylesheet">
<style>
:root{
  --blue:#1487d4;
  --blue-deep:#0c5fa3;
  --navy:#1f5a8c;
  --box:#1473b5;
  --orange:#f47c20;
  --ink:#3a3a3a;
  --grey:#ececec;
  --grey-title:#8a8a8a;
  --white:#ffffff;
}
*{margin:0;padding:0;box-sizing:border-box}
html,body{width:1200px;height:777px;overflow:hidden;background:var(--white)}
.spread{position:relative;width:1200px;height:777px;overflow:hidden;font-family:"PT Sans",sans-serif;color:var(--ink)}
.page-left{position:absolute;left:0;top:0;width:600px;height:720px;background:var(--white)}
.page-right{position:absolute;left:600px;top:0;width:600px;height:720px;background:linear-gradient(90deg,#e2e2e2,#f6f6f6 12%,#f6f6f6)}
.header-art{position:absolute;left:0;top:0}
.title-svg{position:absolute;left:0;top:0;overflow:visible}
.display{font-family:"Saira Extra Condensed","Arial Narrow",sans-serif}
.head{font-family:"Saira Condensed","Arial Narrow",sans-serif;font-weight:600;fill:var(--navy)}
.buy-questions{position:absolute;left:172px;top:247px;font-size:10px;line-height:14px;white-space:nowrap}
.buy-questions .lead{color:var(--blue);font-weight:700}
.look-box{position:absolute;left:37px;top:300px;width:213px;height:409px;background:var(--box);border-radius:8px;color:var(--white);padding:18px 15px 0 16px;font-family:"PT Sans Narrow",sans-serif;font-size:10.4px;line-height:14.6px;text-align:justify}
.look-box h3{font-family:"PT Sans",sans-serif;font-size:13.5px;font-weight:400;margin-bottom:12px;text-align:left}
.look-item{margin-bottom:9px}
.tag{display:inline-block;font-family:"PT Sans",sans-serif;font-weight:700}
.tag .letter{background:#1c2f3f;padding:0 3px}
.tag .word{background:var(--orange);padding:0 10px 0 3px;clip-path:polygon(0 0,100% 0,88% 100%,0 100%)}
.body-col{position:absolute;left:264px;top:305px;width:284px;font-family:"PT Sans Narrow",sans-serif;font-size:10.4px;line-height:14.6px;text-align:justify}
.body-col p{margin-bottom:8px}
.body-col .intro{color:var(--blue)}
.body-col b{color:var(--blue);font-weight:700}
.bullets{list-style:none;font-size:9.6px;line-height:13px}
.bullets li{padding-left:8px;position:relative}
.bullets li::before{content:"•";position:absolute;left:0;color:#888}
.bullets .sub{padding-left:18px}
.bullets .sub::before{left:10px}
.finance{position:absolute;left:647px;top:92px;width:520px}
.manage{position:absolute;left:647px;top:210px;width:520px}
.strategies-band{position:absolute;left:600px;top:348px;width:600px;height:372px;background:var(--grey)}
.growth-art{position:absolute;left:600px;top:520px;width:253px;height:200px;background:linear-gradient(160deg,rgba(236,236,236,0) 15%,#f2b05a 50%,#7fb96a 82%,#6a9a4e)}
.strat-list{position:absolute;left:862px;top:0;width:300px;height:720px;list-style:none}
.strat-list li{position:absolute;left:0;width:300px}
.strat-list .num{font-family:"Saira Condensed","Arial Narrow",sans-serif;font-weight:600;font-size:19px;color:var(--navy)}
.strat-list .lbl{font-family:"PT Sans Narrow",sans-serif;font-weight:700;font-size:11px;color:var(--navy)}
.strat-list .detail{font-size:8.4px;line-height:11.5px;padding-left:8px;color:var(--ink)}
.footer{position:absolute;left:0;top:720px;width:1200px;height:57px;background:linear-gradient(90deg,var(--blue) 0,#1e8fdb 50%,var(--blue-deep) 50%,var(--blue) 58%)}
.footer .bar{position:absolute;left:0;top:27px;width:43px;height:6px;background:var(--white)}
.footer .title{position:absolute;left:51px;top:22px;color:var(--white);font-size:11px;letter-spacing:.3px}
.footer .credit{position:absolute;right:27px;top:22px;color:var(--white);font-size:9.6px}
.footer .credit b{font-weight:700}
</style>
</head>
<body>
<div class="spread">
  <section class="page-left">
    <svg class="header-art" width="600" height="216" viewBox="0 0 600 216" aria-hidden="true">
      <defs>
        <linearGradient id="hdr" x1="0" x2="1">
          <stop offset="0" stop-color="#1590dc"/>
          <stop offset=".75" stop-color="#1a86d2"/>
          <stop offset="1" stop-color="#0c5fa3"/>
        </linearGradient>
      </defs>
      <rect width="600" height="216" fill="url(#hdr)"/>
      <polygon points="0,72 72,72 72,143 143,143 143,216 0,216" fill="#ffffff"/>
      <polygon points="72,72 108,143 72,143" fill="#0e5fa6"/>
      <polygon points="143,143 178,216 143,216" fill="#0e5fa6"/>
    </svg>

    <div class="buy-questions">
      <div class="lead">• Value Add - Key questions when considering a property:</div>
      <div>• Who owns it? &nbsp; • How long have they owned it? &nbsp;• Why are they selling it?</div>
    </div>

    <aside class="look-box">
      <h3>What to look for:</h3>
      <p class="look-item"><span class="tag"><span class="letter">A.</span><span class="word">Poor management</span></span> typically by individual owners, families, or out of state management.</p>
      <p class="look-item"><span class="tag"><span class="letter">B.</span><span class="word">Under market rents</span></span> rates significantly below comparable prices in the area.</p>
      <p class="look-item"><span class="tag"><span class="letter">C.</span><span class="word">Deferred maintenance</span></span> this can be a sign of a motivated or “burned-out” seller. Light exterior and interior upgrades, e.g., paint, landscaping, carpet replacement, fixture and appliance upgrades, will have a significant impact.</p>
      <p class="look-item"><span class="tag"><span class="letter">D.</span><span class="word">High vacancy</span></span> often due to poor marketing.</p>
      <p class="look-item"><span class="tag"><span class="letter">E.</span><span class="word">Motivated sellers</span></span> allows for negotiation a lower price. Common motivators include divorce, bankruptcy, retirement, inherited properties, new investment opportunity, burnout, etc.</p>
      <p class="look-item"><span class="tag"><span class="letter">F.</span><span class="word">Owner paid utilities</span></span> allows for significant upside in income through implementing Ratio Utility Business System (RUBS)</p>
    </aside>

    <div class="body-col">
      <p class="intro">By tackling these issues, we will successfully reposition the property, which will significantly increase the income. As a result, <b>the value of the property</b> will also increase.</p>
      <p><b>Property Class</b> - B and C class properties in A and B neighborhoods - Prefer 1980’s or newer.</p>
      <p>These properties tend to house blue collar workers; don’t compete with new(er) construction; and don’t share the same challenges as C and D properties in C and D neighborhoods, which can encounter issues with crime, major disrepair, and increased vulnerability to economic downturns.</p>
      <p><b>Market Analysis</b> - Target emerging markets with population and job growth; low to median cost of housing which allows rent growth (e.g., Columbus, Oklahoma, Atlanta, Dallas, Phoenix); median income of ~$35k/ yr; and landlord and business friendly rules and regulations (e.g., Ohio, Texas, Florida, Oklahoma, Colorado).</p>
      <p><b>Scale</b> - 60+ units to support effective, third-party professional management. Additionally, targeting 60+units will increase the likelihood of stability by creating a buffer against tenant turnover and other unplanned expenses.</p>
      <p><b>Cash flow</b> - The property must generate cash flow from day one, before value add strategies are deployed.</p>
      <p>Buy on <strong>actual numbers</strong> instead of on pro forma analysis, which project or estimate financial return</p>
    </div>
  </section>

  <section class="page-right"></section>

  <div class="finance">
    <ul class="bullets">
      <li><strong>Longterm debt</strong> - with long terms and amortization periods.</li>
      <li><strong>Non-recourse</strong> if possible. e.g ., Keystone Agency, Meridian Agency, Local/Regional lenders. There is an extremely low foreclosure rate for Keystone and Meridian underwritten properties (1%-2%).</li>
      <li><strong>No prepayment penalty.</strong></li>
      <li><strong>No due on sale clause.</strong></li>
    </ul>
  </div>

  <div class="manage">
    <ul class="bullets">
      <li><strong>Third-Party Management with experience in this specific class of multifamily real estate.</strong></li>
      <li class="sub">Sizable but not too large that our property gets lost.</li>
      <li class="sub">Only in property management, not acquisition or development so that there is no conflict of interest.</li>
      <li><strong>Use of Sole Purpose Entity Structures, e.g., LLC’s for asset protection.</strong></li>
      <li><strong>Optimization through use of systems.</strong></li>
      <li><strong>Tenant satisfaction</strong> - Ensure great customer service to the tenant, e.g., 24 hour response to maintenance requests, cleanliness, and security. Happy tenants who feel heard and cared for, don’t leave, which limits tenant turnover, and lowers expenses.</li>
      <li><strong>Increase the “curb appeal”</strong> - Freshened exterior with modern paint schemes, landscaping, and new signage. Rebranding with a name change, webpage, etc.</li>
    </ul>
  </div>

  <div class="strategies-band"></div>
  <div class="growth-art" role="img" aria-label="Illustration of a rising red arrow over stacks of gold coins above a row of colourful apartment buildings and trees"></div>

  <svg class="title-svg" width="1200" height="720" viewBox="0 0 1200 720">
    <text class="display" x="376" y="120" font-size="72" font-weight="300" fill="#1f5a8c" textLength="140" lengthAdjust="spacingAndGlyphs">3 STEPS</text>
    <text class="display" x="375" y="164" font-size="46" fill="#ffffff" textLength="141" lengthAdjust="spacingAndGlyphs">FOR SUCCESS</text>
    <text class="head" x="52" y="268" font-size="30" textLength="102" lengthAdjust="spacingAndGlyphs">1. Buy Right:</text>
    <text class="head" x="646" y="79" font-size="28" textLength="140" lengthAdjust="spacingAndGlyphs">2. Finance Right:</text>
    <text class="head" x="646" y="198" font-size="28" textLength="142" lengthAdjust="spacingAndGlyphs">3. Manage Right:</text>
    <text class="display" x="646" y="420" font-size="35" fill="#8a8a8a" textLength="150" lengthAdjust="spacingAndGlyphs">6 STRATEGIES FOR</text>
    <text class="display" x="646" y="466" font-size="60" fill="#1487d4" textLength="150" lengthAdjust="spacingAndGlyphs">INCREASING</text>
    <text class="display" x="646" y="512" font-size="60" fill="#1487d4" textLength="94" lengthAdjust="spacingAndGlyphs">INCOME</text>
  </svg>

  <ol class="strat-list">
    <li style="top:390px"><span class="num">1</span><span class="lbl">. Fill vacant units at market rate</span>
      <div class="detail">• After light renovation (&lt; $1,000 per unit) - modern, two-tone paint schemes (white trim, taupe / light grey walls); vinyl wood plank flooring to replace carpet; cleaning of existing carpet.</div></li>
    <li style="top:472px"><span class="num">2</span><span class="lbl">. Employ RUBS, where applicable</span>
      <div class="detail">• Pre-calculated formula for billing back a tenant’s utilities.<br>• Water, sewer, trash, gas/electric.</div></li>
    <li style="top:531px"><span class="num">3</span><span class="lbl">. Gradually raise existing tenants to market rate AFTER adding value</span>
      <div class="detail">• Improve the exterior “curb appeal” - power washing, landscaping, painting. Inexpensive and effective.</div></li>
    <li style="top:602px"><span class="num">4</span><span class="lbl">. Fees - Pet fees; deposits; late fees (without exception); move-in fees</span></li>
    <li style="top:652px"><span class="num">5</span><span class="lbl">. Laundry machines</span></li>
    <li style="top:689px"><span class="num">6</span><span class="lbl">. Lower expenses through renegotiation of contracts</span></li>
  </ol>

  <footer class="footer">
    <span class="bar"></span>
    <span class="title">MULTIFAMILY CASHFLOW INVESTMENT STRATEGY</span>
    <span class="credit"><b>Marlena Caldwell</b> &nbsp;| &nbsp;Real Estate Investor</span>
  </footer>
</div>
</body>
</html>
```